Create a flyer design (10cm X 21cm) for an aquarium in France

We are a public aquarium in France and we want announcing the events of christmas holidays
We invite you to create our flyer recto (just the front side).

The size of this flyer is : 10cm X 21cm
Have a look on flyer.doc to know texts...
We want also get the flyer in original version (.psd, .ai) please.

We remain at your disposal for any question.
Thanks.

Industry/Entity Type

Events

Requirements
Must have
• The text must be written in french, you will find attached all the text that you have to fill in the flyer.
• You also have to use our logo in the top or in the bottom of the flyer (2 versions of the logo four color or black and white version. According your design you can use one of them)
• You must specify our website and our adress.
• Have a look on flyer.doc to know texts...

```html
<!DOCTYPE html>
<html lang="fr">
<head>
<meta charset="utf-8">
<title>Vos vacances de Noël à l'aquarium</title>
<link rel="stylesheet" href="https://fonts.googleapis.com/css2?family=Raleway:wght@200&family=Courgette&family=Quicksand:wght@400;500;700&family=Signika:wght@600;700&display=swap">
<style>
  :root{
    --ink:#4a4a4a;
    --white:#ffffff;
    --deep:#0a2466;
    --navy:#0b3584;
    --sea-top:#25407e;
    --sea-mid:#2a93bd;
    --sea-light:#5cc6d8;
    --coral:#c8352e;
    --teal:#1fa9b8;
    --teal-dark:#0f7488;
    --orange:#f39323;
    --orange-dark:#d9741a;
    --yellow:#f8c42a;
    --lime:#d4df38;
    --pink:#e3177f;
    --green:#a6c93a;
  }
  *{margin:0;padding:0;box-sizing:border-box}
  html,body{width:1200px;height:2521px;overflow:hidden;background:var(--deep)}
  .flyer{position:relative;width:1200px;height:2521px;overflow:hidden;font-family:"Quicksand",sans-serif}

  .sea{position:absolute;inset:0;background:linear-gradient(180deg,var(--sea-top) 0%,#2f5f9c 12%,var(--sea-mid) 28%,var(--sea-light) 40%,#3ea2c4 60%,#2a6fa6 80%,var(--deep) 100%)}
  .photo{position:absolute;left:0;top:730px;width:1200px;height:1380px;
    background:linear-gradient(160deg,#3fa9c8 0%,#f08a3c 22%,#c83a32 45%,#b9272e 58%,#6f8a6a 75%,#2d6d9c 100%)}

  .title{display:block;position:absolute;left:0;width:100%;text-align:center;color:var(--white)}
  .title-top{top:88px;font-family:"Raleway",sans-serif;font-weight:200;font-size:124px;letter-spacing:1px;line-height:1}
  .title-script{top:228px;font-family:"Courgette",cursive;font-size:118px;line-height:1.1;font-weight:400}

  .lens{position:absolute;left:0;width:1200px}
  .lens svg{position:absolute;left:0;top:0}
  .lens-text{position:absolute;left:0;width:100%;text-align:center;color:var(--white);font-weight:500;font-size:43px;line-height:1.3}
  .lens-teal{top:410px;height:220px}
  .lens-teal .lens-text{top:62px}
  .lens-orange{top:590px;height:240px}
  .lens-orange .lens-text{top:58px}

  .event{position:absolute;z-index:2;text-align:center;font-size:46px;line-height:1.22;color:var(--white);font-weight:400}
  .event strong{font-weight:700}
  .event-dive{left:0;top:1345px;width:832px;height:165px;background:var(--yellow);color:var(--ink);transform:rotate(-1deg);padding-top:20px}
  .event-shark{left:0;top:1502px;width:843px;height:165px;background:var(--lime);color:var(--ink);transform:rotate(-1deg);padding-top:20px}
  .event-night{left:370px;top:1682px;width:840px;height:160px;background:var(--orange);transform:rotate(-1.5deg);padding-top:24px}
  .event-fish{left:372px;top:1835px;width:840px;height:160px;background:var(--pink);transform:rotate(-1deg);padding-top:24px}
  .event-taste{left:345px;top:1995px;width:865px;height:162px;background:var(--green);transform:rotate(-1deg);padding-top:22px}

  .footer{position:absolute;left:0;top:2100px;width:1200px;height:421px;background:linear-gradient(180deg,var(--deep) 0%,var(--navy) 60%,#1a6cb8 100%);font-family:"Signika",sans-serif}
  .brand{position:absolute;left:84px;top:95px;color:var(--white);font-weight:700;font-size:118px;line-height:.98;font-family:"Quicksand",sans-serif}
  .brand span{display:block;padding-left:30px}
  .address{position:absolute;left:730px;top:85px;width:340px;text-align:center;color:var(--white);font-style:normal;font-weight:600;font-size:37px;line-height:1.48}
  .website{position:absolute;left:0;width:100%;top:340px;text-align:center;color:var(--white);font-weight:600;font-size:37px}
</style>
</head>
<body>
<main class="flyer">
  <div class="sea" role="img" aria-label="Fond sous-marin bleu avec coraux"></div>
  <div class="photo" role="img" aria-label="Photo sous-marine : plongeur déguisé en Père Noël nourrissant des poissons tropicaux parmi les coraux"></div>

  <h1>
    <span class="title title-top">VOS VACANCES</span>
    <span class="title title-script">de Noël à l'aquarium</span>
  </h1>

  <div class="lens lens-teal">
    <svg width="1200" height="220" viewBox="0 0 1200 220" aria-hidden="true">
      <path d="M95 118 Q560 -30 1095 78 Q600 260 95 118Z" fill="var(--teal-dark)"/>
      <path d="M95 118 Q560 -30 1095 78 Q600 150 95 118Z" fill="var(--teal)"/>
    </svg>
    <p class="lens-text">Animations « bassin tactile »<br>commentées plusieurs fois par jour</p>
  </div>

  <div class="lens lens-orange">
    <svg width="1200" height="240" viewBox="0 0 1200 240" aria-hidden="true">
      <path d="M0 85 Q560 -20 1200 60 Q640 300 0 85Z" fill="var(--orange-dark)"/>
      <path d="M0 85 Q560 -20 1200 60 Q620 150 0 85Z" fill="var(--orange)"/>
    </svg>
    <p class="lens-text">Nourrissages commentés de nos espèces<br>aquatiques chaque après-midi</p>
  </div>

  <p class="event event-dive">Plongée du Père-Noël<br>les <strong>22 et 23 décembre</strong></p>
  <p class="event event-shark">Atelier scientifique sur les Requins<br><strong>lundi 28 décembre</strong></p>
  <p class="event event-night">Nocturne, une visite drôle et décalée,<br><strong>mardi 29 décembre</strong></p>
  <p class="event event-fish">Fish manucure,<br>les <strong>29, 30 et 31 décembre</strong></p>
  <p class="event event-taste">Dégustation vitaminée,<br><strong>les 2 et 3 janvier</strong></p>

  <footer class="footer">
    <p class="brand">Aquarium<span>de Kerbrat</span></p>
    <address class="address">
      Aquarium de Kerbrat<br>
      14, rue des Mouettes<br>
      56100 KERBRAT<br>
      02 97 12 34 56
    </address>
    <p class="website">Retrouvez toutes les informations via aquariumdekerbrat.fr</p>
  </footer>
</main>
</body>
</html>
```